Veltrano - Mechanic/Collision Center Business Card

We're looking for a business card design for our mechanic/ collision repair shop.

Can be with colours or monochromatic.

See the attached files.

Many thanks

```html
<!DOCTYPE html>
<html lang="pt">
<head>
<meta charset="utf-8">
<title>Veltrano – Business Card</title>
<link href="https://fonts.googleapis.com/css2?family=Arvo:wght@700&family=Cabin:wght@500&family=Roboto+Condensed:wght@700&display=swap" rel="stylesheet">
<style>
  :root {
    --bg-center: #2b7aa6;
    --bg-edge: #2c3f4c;
    --card-fill: rgba(60, 150, 200, 0.35);
    --card-stroke: #19a4ea;
    --text: #ffffff;
    --logo-grey: #4b4f55;
    --rule: #4fb8ee;
  }
  * { margin: 0; padding: 0; box-sizing: border-box; }
  html, body { width: 1200px; height: 1200px; overflow: hidden; }
  body {
    position: relative;
    background: radial-gradient(ellipse at 50% 45%, var(--bg-center) 0%, #27688c 45%, var(--bg-edge) 100%);
    color: var(--text);
  }
  .card {
    position: absolute;
    top: 251px;
    width: 397px;
    height: 697px;
    border: 3px solid var(--card-stroke);
    border-radius: 0 75px 0 75px;
    background: var(--card-fill);
    box-shadow: 0 30px 60px rgba(10, 40, 60, 0.35);
  }
  .card--front { left: 199px; }
  .card--back { left: 604px; }

  .brand-name {
    position: absolute;
    left: 0; right: 0;
    text-align: center;
    font-family: "Arvo", serif;
    font-weight: 700;
    color: var(--logo-grey);
  }
  .card--front .brand-name { top: 335px; font-size: 60px; }
  .card--back .brand-name { top: 245px; font-size: 44px; }

  .holder-name {
    position: absolute;
    left: 44px; top: 12px;
    font-family: "Arvo", serif;
    font-weight: 700;
    font-size: 29px;
    letter-spacing: 0.5px;
  }
  .holder-phone {
    position: absolute;
    right: 58px; top: 50px;
    font-family: "Roboto Condensed", sans-serif;
    font-weight: 700;
    font-size: 26px;
  }
  .company-row {
    position: absolute;
    left: 6px; right: 6px; top: 398px;
    display: flex; align-items: center; gap: 8px;
    font-family: "Arvo", serif; font-weight: 700; font-size: 23px;
    white-space: nowrap;
  }
  .phone-row {
    position: absolute;
    left: 12px; right: 12px; top: 438px;
    display: flex; align-items: center; gap: 12px;
    font-family: "Roboto Condensed", sans-serif; font-weight: 700; font-size: 22px;
  }
  .double-rule {
    flex: 1; height: 5px;
    border-top: 1px solid var(--rule);
    border-bottom: 1px solid var(--rule);
  }
  .phone-row .icon { width: 26px; height: 26px; }
  .contact-list {
    position: absolute; left: 30px; top: 508px;
    list-style: none;
    font-family: "Cabin", sans-serif; font-weight: 500; font-size: 20px;
  }
  .contact-list li { display: flex; align-items: center; height: 37px; }
  .contact-list .icon { width: 22px; height: 22px; margin-right: 14px; flex: none; }
</style>
</head>
<body>
  <section class="card card--front">
    <div class="brand-name">Veltrano</div>
  </section>

  <section class="card card--back">
    <div class="holder-name">RUI MATOS</div>
    <div class="holder-phone">910000482</div>

    <div class="brand-name">Veltrano</div>

    <div class="company-row">
      <span class="double-rule"></span>
      <span>Veltrano, LDA</span>
      <span class="double-rule"></span>
    </div>
    <div class="phone-row">
      <span class="double-rule"></span>
      <svg class="icon" viewBox="0 0 26 26" aria-hidden="true">
        <circle cx="13" cy="13" r="11.5" fill="none" stroke="#fff" stroke-width="2"/>
        <path d="M9 7.5l2.2 2.6-1.3 1.6c.8 1.8 2 3 3.8 3.8l1.6-1.3 2.6 2.2-1.4 2c-4.5-.6-8.5-4.6-9.1-9.1z" fill="#fff"/>
      </svg>
      <span>210004517</span>
      <span class="double-rule"></span>
    </div>

    <ul class="contact-list">
      <li>
        <svg class="icon" viewBox="0 0 22 22" aria-hidden="true"><circle cx="11" cy="7" r="4" fill="none" stroke="#fff" stroke-width="2"/><path d="M11 11v5M5 18h12" stroke="#fff" stroke-width="2" fill="none"/></svg>
        Rua das Oficinas. 42
      </li>
      <li>
        <svg class="icon" viewBox="0 0 22 22" aria-hidden="true"><rect x="2" y="5" width="18" height="13" rx="2" fill="#fff"/></svg>
        1900-000 Lisboa
      </li>
      <li>
        <svg class="icon" viewBox="0 0 22 22" aria-hidden="true"><rect x="2" y="5" width="18" height="12" fill="none" stroke="#fff" stroke-width="1.8"/><path d="M2 5l9 7 9-7" fill="none" stroke="#fff" stroke-width="1.8"/></svg>
        veltrano.oficina@mail.pt
      </li>
      <li>
        <svg class="icon" viewBox="0 0 22 22" aria-hidden="true"><rect x="3" y="3" width="16" height="16" rx="3" fill="#fff"/></svg>
        www.social.pt/veltrano
      </li>
    </ul>
  </section>
</body>
</html>
```